National Training and assessment company needs a website

Create a 4 page website, simple but professional, the company provides training services to industry, resumes'/ CVs, personnel skill assessment, workplace skills profiling and develops manufactures and supplies training equipment for electrical/engineering training, Company title is Toren K Pty Ltd and also trades under BRW & Associates. letterheads etc all are done using dark green
Reason: Due to work commitments will be interstate from the 26/02 til 05/03/14
Target Market(s)
The market is broad covering the general public, secondary colleges and corporate sector
Industry/Entity Type
Training
Look and feel

```html
<!DOCTYPE html>
<html lang="en">
<head>
<meta charset="utf-8">
<title>Toren K Pty Ltd</title>
<link rel="stylesheet" href="https://fonts.googleapis.com/css2?family=Gelasio&family=Open+Sans:wght@400&display=swap">
<style>
  :root {
    --green-dark: #17524a;
    --green-text: #1c5a50;
    --green-light: #7cb44a;
    --green-pale: #9fc77a;
    --grey-bg: #e6e7e8;
    --white: #ffffff;
  }
  * { margin: 0; padding: 0; box-sizing: border-box; }
  html, body { width: 1179px; height: 1200px; overflow: hidden; }
  body { background: var(--grey-bg); font-family: "Open Sans", Arial, sans-serif; color: var(--green-text); position: relative; }

  .top-band { position: absolute; left: 0; top: 0; width: 1179px; height: 31px; background: var(--green-dark); }

  .brand { position: absolute; left: 50px; top: 104px; display: flex; align-items: center; gap: 14px; color: var(--green-dark); }
  .brand-mark { width: 26px; height: 26px; background: var(--green-dark); }
  .brand-name { font-family: "Open Sans", Arial, sans-serif; font-size: 36px; line-height: 40px; }

  .search { position: absolute; left: 545px; top: 72px; display: flex; gap: 9px; }
  .search-input { width: 384px; height: 47px; border: 3px solid var(--green-dark); border-radius: 5px; background: var(--white); }
  .search-button { width: 191px; height: 48px; border-radius: 5px; background: linear-gradient(to bottom, #6f9e95 0%, #6f9e95 45%, var(--green-dark) 45%); color: var(--white); display: flex; align-items: center; justify-content: center; gap: 12px; font-size: 20px; letter-spacing: 0.5px; }

  .main-nav { position: absolute; right: 50px; top: 170px; display: flex; font-size: 14.6px; color: var(--green-dark); }
  .main-nav span { margin-left: 16px; }
  .main-nav span.wide { margin-left: 20px; }

  .hero { position: absolute; left: 0; top: 228px; width: 1179px; height: 544px;
    background: linear-gradient(to bottom, #4b3f9a 0%, #6a55b4 30%, #9c7bcb 55%, #d7a0c9 72%, #f4b48a 84%, #e8792a 93%, #2a1d22 100%); }
  .hero-title { position: absolute; left: 50px; top: 50px; font-family: "Gelasio", Georgia, serif; font-weight: 400; font-size: 28px; line-height: 30px; color: var(--white); }
  .hero-title .indent { display: block; padding-left: 108px; }

  .about { position: absolute; left: 50px; top: 819px; width: 705px; font-size: 13.6px; line-height: 22.3px; color: var(--green-text); }
  .about ul { list-style: none; }
  .about li::before { content: "·"; margin-right: 7px; }

  .divider { position: absolute; left: 769px; top: 823px; width: 1px; height: 278px; background: var(--green-light); }

  .contact { position: absolute; left: 791px; top: 826px; }
  .contact-name { font-size: 26px; line-height: 32px; color: var(--green-light); }
  .contact-details { margin-top: 18px; font-size: 14.6px; line-height: 20.3px; color: var(--green-pale); }

  .footer-band { position: absolute; left: 0; top: 1155px; width: 1179px; height: 45px; background: var(--green-dark); display: flex; justify-content: center; align-items: center; gap: 9px; }
</style>
</head>
<body>
  <div class="top-band"></div>

  <header>
    <div class="brand">
      <div class="brand-mark"></div>
      <div class="brand-name">Toren K Pty Ltd</div>
    </div>

    <div class="search">
      <div class="search-input"></div>
      <div class="search-button">
        <svg width="30" height="30" viewBox="0 0 30 30" aria-hidden="true">
          <circle cx="15" cy="15" r="13" fill="none" stroke="#fff" stroke-width="2"/>
          <circle cx="13.5" cy="13.5" r="5" fill="none" stroke="#fff" stroke-width="2"/>
          <line x1="17" y1="17" x2="21" y2="21" stroke="#fff" stroke-width="2.4" stroke-linecap="round"/>
        </svg>
        <span>SEARCH</span>
      </div>
    </div>

    <nav class="main-nav">
      <span>HOME</span><span>ABOUT US</span><span>SERVICES</span><span class="wide">ASSESSMENTS</span><span class="wide">WORKPLACES</span><span class="wide">LINKS</span><span>CONTACT US</span>
    </nav>
  </header>

  <section class="hero" role="img" aria-label="Family silhouetted against a purple and orange sunset sky">
    <h1 class="hero-title">Toren K Pty Ltd is dedicated<span class="indent">to providing quality customer focused service in all its ventures.</span></h1>
  </section>

  <main class="about">
    <p>Toren K Pty Ltd is dedicated to providing quality customer focused service in all its ventures. Toren K core business is workplace training assessment with broader services which include:</p>
    <ul>
      <li>Employer Workplace skills profiling</li>
      <li>Employee skills profiling (Competency Profiling)</li>
      <li>Workplace training and Assessment</li>
      <li>Resume and Curricula Vita compilation</li>
    </ul>
    <p>The business was established in 1996 trading as BRW &amp; Associates and registered as a company (Toren K) in 2002. &nbsp;Over this time Toren K trading as BRW &amp; Associates has built a client base Australia wide aligning engineering trades people against the National training agenda therefore enhancing their employment/career opportunities. &nbsp;The company has built a client base of Ex serving RAN engineering members assisting to align military skills to the industrial sector. &nbsp;This has extended to the general engineering public keen to update qualifications and align to the National training agenda in competency terms.</p>
  </main>

  <div class="divider"></div>

  <aside class="contact">
    <div class="contact-name">Toren K Pty Ltd</div>
    <div class="contact-details">
      P.O. Box 5280<br>
      Ashgrove Vale, Vic. 3208<br>
      T. 03 9555 0142<br>
      F. 03 9555 0187<br>
      M. 0400 555 261<br>
      E. torenk@greenmail.example.au
    </div>
  </aside>

  <footer class="footer-band">
    <svg width="27" height="27" viewBox="0 0 27 27" aria-hidden="true"><circle cx="13.5" cy="13.5" r="12" fill="none" stroke="#fff" stroke-width="2"/></svg>
    <svg width="27" height="27" viewBox="0 0 27 27" aria-hidden="true"><circle cx="13.5" cy="13.5" r="12" fill="none" stroke="#fff" stroke-width="2"/></svg>
    <svg width="27" height="27" viewBox="0 0 27 27" aria-hidden="true"><circle cx="13.5" cy="13.5" r="12" fill="none" stroke="#fff" stroke-width="2"/></svg>
    <svg width="27" height="27" viewBox="0 0 27 27" aria-hidden="true"><circle cx="13.5" cy="13.5" r="12" fill="none" stroke="#fff" stroke-width="2"/></svg>
  </footer>
</body>
</html>
```